Corporate Trainning business needs PPT template for sales, reports and projects

Create a power point template with own design and rich in distinctness of our brand, logo and industry (corporate training). Enough slides templates to use for sales, reports and projects development: flowcharts, roadmaps, bullets, service categories, description box, title & subtitle slides, bar & pie charts, calendars, gantt, some basic shapes and icons (training, education, elearning, etc related).
Enclose: color palette, set of logo for different uses and ppt presentation with some ideas and slide templates. The ppt hope could help, but I trust in your experience and creativity.

Target Market(s)

Company training

Industry/Entity Type

Training - Education

Font styles to use
Sans Serif

Requirements
Nice to have
• Relative to training icons

```html
<!DOCTYPE html>
<html lang="en">
<head>
<meta charset="utf-8">
<title>Veltrin Presentation Template</title>
<link href="https://fonts.googleapis.com/css2?family=Montserrat:wght@400;500;700;800&display=swap" rel="stylesheet">
<style>
:root{
  --navy:#0b2d5b;
  --teal:#0f8ca8;
  --teal-light:#7cc7d8;
  --yellow:#f0c400;
  --grey:#6e6e6e;
  --paper:#ffffff;
  --mist:#d9dadd;
  --soft:#f3f4f6;
}
*{box-sizing:border-box;margin:0;padding:0}
html,body{width:751px;height:1200px;overflow:hidden}
body{font-family:"Montserrat",Arial,sans-serif;background:linear-gradient(#e4e6ea,#cfd1d5 40%,#c9cacd);position:relative;color:var(--navy)}
.brand{font-weight:500;color:var(--navy);letter-spacing:-.02em;line-height:1}
.brand-main{position:absolute;left:600px;top:40px;font-size:32px}
.brand-main::before{content:"";display:inline-block;width:26px;height:26px;border-radius:50%;background:var(--yellow);margin-right:8px;vertical-align:-3px}
.slide{position:absolute;width:236px;height:133px;background:var(--paper);overflow:hidden}
.hero{left:150px;top:80px;width:400px;height:225px;box-shadow:0 10px 30px rgba(0,0,0,.18)}
.photo{position:absolute}
.title-photo{right:0;top:0;width:52%;height:100%;background:linear-gradient(135deg,#7fa9b8,#e8ecef 45%,#f4f1ea);border-bottom-left-radius:60% 100%}
.title-photo::after{content:"";position:absolute;right:0;bottom:22%;width:22%;height:30%;background:var(--yellow);opacity:.85;border-radius:18% 0 0 18%}
.slide-logo{position:absolute;left:13px;top:12px;font-size:13px}
.title-band{position:absolute;left:0;top:41px;width:56%;height:50px;border-radius:0 14px 14px 0;padding:6px 0 0 13px;color:#fff}
.title-band .t1{font-weight:800;font-size:11px;letter-spacing:.02em;line-height:1.1}
.title-band .t2{font-size:11px;line-height:1.1}
.title-band .t3{font-size:4.4px;margin-top:3px}
.date{position:absolute;left:13px;top:106px;font-size:2.8px;color:var(--grey)}
.bottom-bar{position:absolute;left:0;bottom:0;width:100%;height:8px;font-size:2.6px;color:#fff;text-align:center;line-height:8px}
.hero .slide-logo{font-size:24px;left:24px;top:22px}
.hero .title-band{top:72px;height:86px;padding:12px 0 0 24px}
.hero .t1{font-size:20px}.hero .t2{font-size:19px}.hero .t3{font-size:7.5px;margin-top:6px}
.hero .date{font-size:5px;left:24px;top:188px}
.hero .bottom-bar{height:14px;font-size:4.5px;line-height:14px}
.is-navy{background:var(--navy)}.is-teal{background:var(--teal)}.is-yellow{background:var(--yellow)}
.band-yellow .t1,.band-yellow .t2{color:var(--yellow)}
.band-dark,.band-dark .t1,.band-dark .t2,.band-dark .t3{color:var(--navy)}
.head{position:absolute;left:9px;top:9px;font-size:7px;color:var(--navy);padding-left:7px;border-left:2px solid var(--yellow);line-height:9px}
.head b{font-weight:700}
.foot-logo{position:absolute;left:6px;bottom:5px;font-size:7.5px}
.foot-logo::before{content:"";display:inline-block;width:6px;height:6px;border-radius:50%;background:var(--yellow);margin-right:2px}
.copy{position:absolute;right:8px;bottom:6px;font-size:2.2px;color:var(--grey)}
.ico{border-radius:50%;display:inline-block;position:relative}
.ico::after{content:"";position:absolute;left:32%;top:32%;width:36%;height:36%;border-radius:50%;border:1px solid #fff}
.note{font-size:2.4px;color:var(--grey);line-height:1.25}
.h{font-size:4.4px;font-weight:400;color:var(--navy)}
.h b{font-weight:700}
.cell{position:absolute;text-align:center;width:60px}
.cell .ico{width:15px;height:15px;margin-bottom:2px}
.val{position:absolute;left:32px;display:flex;gap:6px;align-items:center;width:180px}
.val .ico{width:20px;height:20px;flex:none}
.feat{position:absolute;left:17px;display:flex;gap:5px;align-items:center}
.feat .ico{width:14px;height:14px;flex:none}
.feat .h{color:var(--yellow)}
.feat .note{color:#cfd8e6}
.step{position:absolute;left:137px;display:flex;gap:8px;width:90px}
.step .date-tag{font-size:3.4px;font-weight:700;color:var(--teal);width:16px;text-align:right}
.step .body{border-left:1px solid #ddd;padding-left:6px;position:relative}
.step .body::before{content:"";position:absolute;left:-2px;top:1px;width:3px;height:3px;background:var(--yellow)}
.lbl{position:absolute;width:55px}
.lbl.r{text-align:left}
.lbl.l{text-align:right}
table{position:absolute;left:14px;top:32px;width:206px;border-collapse:collapse;font-size:2.8px}
th{height:10px;color:#fff;font-weight:700;text-align:center}
th:first-child{text-align:left;padding-left:2px}
td{height:12px;border-bottom:1px solid #eee;text-align:center;font-weight:700}
td:first-child{text-align:left;padding-left:2px;color:var(--navy)}
tr:nth-child(even) td{background:#f6f6f6}
.yes{color:#3aa55a}.no{color:#d9332b}
.pct{position:absolute;text-align:center;width:60px;top:30px}
.pct .city{font-size:4.4px;font-weight:700;margin-top:1px}
.opt{position:absolute;left:137px;display:flex;gap:5px;align-items:center}
.opt .ico{width:15px;height:15px}
.contact{position:absolute;left:16px;top:80px;font-size:3px;color:var(--grey);line-height:2}
.contact b{color:var(--navy);font-size:4.4px}
</style>
</head>
<body>

<div class="brand brand-main">Veltrin</div>

<!-- hero title slide -->
<section class="slide hero">
  <div class="photo title-photo" role="img" aria-label="Photo of a hand drawing a line chart with a blue pen"></div>
  <div class="brand slide-logo">Veltrin</div>
  <div class="title-band is-teal"><div class="t1">PRESENTATION</div><div class="t2">Title Goes Here!</div><div class="t3">Presentation Subtitle Goes Here!</div></div>
  <div class="date">Sunday, August 14, 2022</div>
  <div class="bottom-bar is-navy">© 2022 Veltrin. All rights reserved.</div>
</section>

<!-- row 1 -->
<section class="slide" style="left:16px;top:489px">
  <div class="photo title-photo" role="img" aria-label="Photo of a hand drawing a line chart"></div>
  <div class="brand slide-logo">Veltrin</div>
  <div class="title-band is-navy band-yellow"><div class="t1">PRESENTATION</div><div class="t2">Title Goes Here!</div><div class="t3">Presentation Subtitle Goes Here!</div></div>
  <div class="date">Sunday, August 14, 2022</div>
  <div class="bottom-bar is-teal">© 2022 Veltrin. All rights reserved.</div>
</section>
<section class="slide" style="left:258px;top:489px">
  <div class="photo title-photo" role="img" aria-label="Photo of a hand drawing a line chart"></div>
  <div class="brand slide-logo">Veltrin</div>
  <div class="title-band is-yellow band-dark"><div class="t1">PRESENTATION</div><div class="t2">Title Goes Here!</div><div class="t3">Presentation Subtitle Goes Here!</div></div>
  <div class="date">Sunday, August 14, 2022</div>
  <div class="bottom-bar is-navy">© 2022 Veltrin. All rights reserved.</div>
</section>
<section class="slide" style="left:501px;top:489px">
  <div class="photo title-photo" role="img" aria-label="Photo of a hand drawing a line chart"></div>
  <div class="brand slide-logo">Veltrin</div>
  <div class="title-band is-teal"><div class="t1">PRESENTATION</div><div class="t2">Title Goes Here!</div><div class="t3">Presentation Subtitle Goes Here!</div></div>
  <div class="date">Sunday, August 14, 2022</div>
  <div class="bottom-bar is-navy">© 2022 Veltrin. All rights reserved.</div>
</section>

<!-- row 2 -->
<section class="slide" style="left:16px;top:629px">
  <div class="head"><b>Veltrin</b> Solutions</div>
  <div class="cell" style="left:31px;top:30px"><span class="ico is-navy"></span><div class="h"><b>Heading</b> Goes Here</div><div class="note">Brief supporting note here.</div></div>
  <div class="cell" style="left:88px;top:30px"><span class="ico is-yellow"></span><div class="h"><b>Heading</b> Goes Here</div><div class="note">Brief supporting note here.</div></div>
  <div class="cell" style="left:145px;top:30px"><span class="ico is-teal"></span><div class="h"><b>Heading</b> Goes Here</div><div class="note">Brief supporting note here.</div></div>
  <div class="cell" style="left:31px;top:70px"><span class="ico is-teal"></span><div class="h"><b>Heading</b> Goes Here</div><div class="note">Brief supporting note here.</div></div>
  <div class="cell" style="left:88px;top:70px"><span class="ico is-navy"></span><div class="h"><b>Heading</b> Goes Here</div><div class="note">Brief supporting note here.</div></div>
  <div class="cell" style="left:145px;top:70px"><span class="ico is-yellow"></span><div class="h"><b>Heading</b> Goes Here</div><div class="note">Brief supporting note here.</div></div>
  <div class="brand foot-logo">Veltrin</div><div class="copy">© 2022 Veltrin. All rights reserved.</div>
</section>
<section class="slide" style="left:258px;top:629px">
  <div class="head"><b>Veltrin</b> Values</div>
  <div class="val" style="top:30px"><span class="ico is-navy"></span><div><div class="h">we love <b>innovations</b></div><div class="note">Brief supporting note for this value goes here.</div></div></div>
  <div class="val" style="top:57px"><span class="ico is-yellow"></span><div><div class="h">we respect the <b>nature</b></div><div class="note">Brief supporting note for this value goes here.</div></div></div>
  <div class="val" style="top:84px"><span class="ico is-teal"></span><div><div class="h">we believe in <b>future</b></div><div class="note">Brief supporting note for this value goes here.</div></div></div>
  <div class="brand foot-logo">Veltrin</div><div class="copy">© 2022 Veltrin. All rights reserved.</div>
</section>
<section class="slide" style="left:501px;top:629px">
  <div style="position:absolute;left:0;top:0;width:117px;height:133px;background:var(--navy)"></div>
  <div class="head" style="color:#fff"><b>Heading</b> Goes Here!</div>
  <div class="feat" style="top:30px"><span class="ico is-yellow"></span><div><div class="h">Feature <b>One</b></div><div class="note">Brief supporting note here.</div></div></div>
  <div class="feat" style="top:50px"><span class="ico is-yellow"></span><div><div class="h">Feature <b>Two</b></div><div class="note">Brief supporting note here.</div></div></div>
  <div class="feat" style="top:70px"><span class="ico is-yellow"></span><div><div class="h">Feature <b>Three</b></div><div class="note">Brief supporting note here.</div></div></div>
  <div class="feat" style="top:90px"><span class="ico is-yellow"></span><div><div class="h">Feature <b>Four</b></div><div class="note">Brief supporting note here.</div></div></div>
  <div class="photo" style="left:121px;top:4px;width:111px;height:114px;background:linear-gradient(135deg,#8fa7bf,#3a4d63 60%,#1d2633)" role="img" aria-label="Photo of a person holding a tablet showing a market chart"></div>
  <div class="brand foot-logo" style="color:#fff">Veltrin</div><div class="copy">© 2022 Veltrin. All rights reserved.</div>
</section>

<!-- row 3 -->
<section class="slide" style="left:16px;top:769px">
  <div style="position:absolute;left:117px;top:0;width:119px;height:133px;background:var(--soft)"></div>
  <div class="photo" style="left:4px;top:4px;width:110px;height:107px;background:linear-gradient(135deg,#d7d3cc,#a59c91 55%,#6b625a)" role="img" aria-label="Overhead photo of a team working around a meeting table"></div>
  <div class="head" style="left:125px">Four Steps <b>Process</b></div>
  <div class="step" style="top:30px"><span class="date-tag">JUN 01</span><div class="body"><div class="h"><b>Start</b> Point</div><div class="note">Brief supporting note here.</div></div></div>
  <div class="step" style="top:51px"><span class="date-tag">JUL 15</span><div class="body"><div class="h"><b>Midpoint</b> One</div><div class="note">Brief supporting note here.</div></div></div>
  <div class="step" style="top:72px"><span class="date-tag">AUG 01</span><div class="body"><div class="h"><b>Midpoint</b> Two</div><div class="note">Brief supporting note here.</div></div></div>
  <div class="step" style="top:93px"><span class="date-tag">SEP 15</span><div class="body"><div class="h"><b>Finish</b></div><div class="note">Brief supporting note here.</div></div></div>
  <div class="brand foot-logo">Veltrin</div><div class="copy">© 2022 Veltrin. All rights reserved.</div>
</section>
<section class="slide" style="left:258px;top:769px">
  <div class="head"><b>Branding</b> Infographics</div>
  <div class="note" style="position:absolute;left:17px;top:26px;width:60px">Marketing builds lasting customer relationships.</div>
  <svg style="position:absolute;left:75px;top:33px" width="80" height="80" viewBox="0 0 80 80">
    <circle cx="40" cy="26" r="24" fill="var(--navy)"/>
    <circle cx="26" cy="50" r="24" fill="var(--teal)" fill-opacity=".95"/>
    <circle cx="54" cy="50" r="24" fill="var(--yellow)" fill-opacity=".95"/>
    <circle cx="40" cy="42" r="13" fill="#3c5675"/>
    <text x="40" y="14" font-size="3" fill="#fff" text-anchor="middle" font-family="Montserrat,sans-serif">Visual Identity</text>
    <text x="14" y="55" font-size="3" fill="#fff" text-anchor="middle" font-family="Montserrat,sans-serif">Brand Tone</text>
    <text x="66" y="55" font-size="3" fill="#fff" text-anchor="middle" font-family="Montserrat,sans-serif">Strategy</text>
  </svg>
  <div class="lbl r note" style="left:150px;top:43px;border-left:1px solid var(--navy);padding-left:2px">Brief supporting note here.</div>
  <div class="lbl l note" style="left:22px;top:85px;border-right:1px solid var(--teal);padding-right:2px">Brief supporting note here.</div>
  <div class="lbl r note" style="left:163px;top:85px;border-left:1px solid var(--yellow);padding-left:2px">Brief supporting note here.</div>
  <div class="brand foot-logo">Veltrin</div><div class="copy">© 2022 Veltrin. All rights reserved.</div>
</section>
<section class="slide" style="left:501px;top:769px">
  <div class="head">Creative <b>Infographics</b></div>
  <svg style="position:absolute;left:84px;top:37px" width="70" height="70" viewBox="0 0 70 70">
    <g fill="none" stroke-width="14" transform="rotate(-90 35 35)">
      <circle cx="35" cy="35" r="24" stroke="var(--navy)" stroke-dasharray="48 150.8"/>
      <circle cx="35" cy="35" r="24" stroke="var(--yellow)" stroke-dasharray="48 150.8" stroke-dashoffset="-51"/>
      <circle cx="35" cy="35" r="24" stroke="var(--teal)" stroke-dasharray="48 150.8" stroke-dashoffset="-102"/>
    </g>
  </svg>
  <div class="lbl r" style="left:157px;top:35px"><div class="h">Title <b>One</b></div><div class="note">Brief supporting note here.</div></div>
  <div class="lbl l" style="left:22px;top:45px"><div class="h">Title <b>Three</b></div><div class="note">Brief supporting note here.</div></div>
  <div class="lbl r" style="left:157px;top:93px"><div class="h">Title <b>Two</b></div><div class="note">Brief supporting note here.</div></div>
  <div class="brand foot-logo">Veltrin</div><div class="copy">© 2022 Veltrin. All rights reserved.</div>
</section>

<!-- row 4 -->
<section class="slide" style="left:16px;top:909px">
  <div class="head">Creative <b>Infographics</b></div>
  <svg style="position:absolute;left:84px;top:34px" width="68" height="68" viewBox="0 0 68 68">
    <g fill="none" stroke-width="14" transform="rotate(-90 34 34)">
      <circle cx="34" cy="34" r="24" stroke="var(--yellow)" stroke-dasharray="23 150.8"/>
      <circle cx="34" cy="34" r="24" stroke="var(--teal)" stroke-dasharray="23 150.8" stroke-dashoffset="-25"/>
      <circle cx="34" cy="34" r="24" stroke="var(--navy)" stroke-dasharray="23 150.8" stroke-dashoffset="-50"/>
      <circle cx="34" cy="34" r="24" stroke="var(--yellow)" stroke-dasharray="23 150.8" stroke-dashoffset="-75"/>
      <circle cx="34" cy="34" r="24" stroke="var(--teal)" stroke-dasharray="23 150.8" stroke-dashoffset="-100"/>
      <circle cx="34" cy="34" r="24" stroke="var(--navy)" stroke-dasharray="23 150.8" stroke-dashoffset="-125"/>
    </g>
  </svg>
  <div class="lbl l" style="left:26px;top:36px"><div class="h"><b>Heading</b> Goes Here</div><div class="note">Brief supporting note here.</div></div>
  <div class="lbl l" style="left:17px;top:60px"><div class="h"><b>Heading</b> Goes Here</div><div class="note">Brief supporting note here.</div></div>
  <div class="lbl l" style="left:26px;top:84px"><div class="h"><b>Heading</b> Goes Here</div><div class="note">Brief supporting note here.</div></div>
  <div class="lbl r" style="left:158px;top:36px"><div class="h"><b>Heading</b> Goes Here</div><div class="note">Brief supporting note here.</div></div>
  <div class="lbl r" style="left:167px;top:60px"><div class="h"><b>Heading</b> Goes Here</div><div class="note">Brief supporting note here.</div></div>
  <div class="lbl r" style="left:158px;top:84px"><div class="h"><b>Heading</b> Goes Here</div><div class="note">Brief supporting note here.</div></div>
  <div class="brand foot-logo">Veltrin</div><div class="copy">© 2022 Veltrin. All rights reserved.</div>
</section>
<section class="slide" style="left:258px;top:909px">
  <div class="head"><b>Table</b> Layout</div>
  <table>
    <tr><th class="is-navy">Heading</th><th style="background:var(--yellow);color:var(--navy)">Column Title 1</th><th class="is-teal">Column Title 2</th><th style="background:var(--teal-light)">Column Title 3</th><th style="background:#666">Column Title 4</th></tr>
    <tr><td>Feature One</td><td class="yes">✓</td><td class="yes">✓</td><td class="yes">✓</td><td class="yes">✓</td></tr>
    <tr><td>Feature Two</td><td class="yes">✓</td><td class="yes">✓</td><td class="yes">✓</td><td class="yes">✓</td></tr>
    <tr><td>Feature Three</td><td class="yes">✓</td><td class="yes">✓</td><td class="yes">✓</td><td class="no">✕</td></tr>
    <tr><td>Feature Four</td><td class="yes">✓</td><td class="yes">✓</td><td class="no">✕</td><td class="no">✕</td></tr>
    <tr><td>Feature Five</td><td class="yes">✓</td><td class="no">✕</td><td class="no">✕</td><td class="no">✕</td></tr>
  </table>
  <div class="brand foot-logo">Veltrin</div><div class="copy">© 2022 Veltrin. All rights reserved.</div>
</section>
<section class="slide" style="left:501px;top:909px">
  <div class="head"><b>Circle</b> Infographics</div>
  <div class="pct" style="left:22px">
    <svg width="50" height="50" viewBox="0 0 50 50"><circle cx="25" cy="25" r="22" fill="none" stroke="#eee" stroke-width="3"/><circle cx="25" cy="25" r="22" fill="none" stroke="var(--navy)" stroke-width="3" stroke-dasharray="88.5 138.2" transform="rotate(-90 25 25)"/><text x="25" y="28" font-size="8" font-weight="700" fill="var(--navy)" text-anchor="middle" font-family="Montserrat,sans-serif">64%</text></svg>
    <div class="city" style="color:var(--navy)">California</div><div class="note">Brief supporting note here.</div></div>
  <div class="pct" style="left:88px">
    <svg width="50" height="50" viewBox="0 0 50 50"><circle cx="25" cy="25" r="22" fill="none" stroke="#eee" stroke-width="3"/><circle cx="25" cy="25" r="22" fill="none" stroke="var(--yellow)" stroke-width="3" stroke-dasharray="113.3 138.2" transform="rotate(-90 25 25)"/><text x="25" y="28" font-size="8" font-weight="700" fill="var(--yellow)" text-anchor="middle" font-family="Montserrat,sans-serif">82%</text></svg>
    <div class="city" style="color:var(--yellow)">Florida</div><div class="note">Brief supporting note here.</div></div>
  <div class="pct" style="left:154px">
    <svg width="50" height="50" viewBox="0 0 50 50"><circle cx="25" cy="25" r="22" fill="none" stroke="#eee" stroke-width="3"/><circle cx="25" cy="25" r="22" fill="none" stroke="var(--teal)" stroke-width="3" stroke-dasharray="130 138.2" transform="rotate(-90 25 25)"/><text x="25" y="28" font-size="8" font-weight="700" fill="var(--teal)" text-anchor="middle" font-family="Montserrat,sans-serif">94%</text></svg>
    <div class="city" style="color:var(--teal)">New York</div><div class="note">Brief supporting note here.</div></div>
  <div class="brand foot-logo">Veltrin</div><div class="copy">© 2022 Veltrin. All rights reserved.</div>
</section>

<!-- row 5 -->
<section class="slide" style="left:138px;top:1049px">
  <div class="head"><b>Chart</b> Slide</div>
  <svg style="position:absolute;left:16px;top:36px" width="100" height="80" viewBox="0 0 100 80" font-family="Montserrat,sans-serif" font-size="2.6" fill="var(--grey)">
    <g stroke="#eee" stroke-width=".4"><line x1="8" y1="2" x2="98" y2="2"/><line x1="8" y1="12" x2="98" y2="12"/><line x1="8" y1="22" x2="98" y2="22"/><line x1="8" y1="32" x2="98" y2="32"/><line x1="8" y1="42" x2="98" y2="42"/><line x1="8" y1="52" x2="98" y2="52"/><line x1="8" y1="62" x2="98" y2="62"/></g>
    <text x="3" y="3">6</text><text x="3" y="13">5</text><text x="3" y="23">4</text><text x="3" y="33">3</text><text x="3" y="43">2</text><text x="3" y="53">1</text><text x="3" y="63">0</text>
    <rect x="13" y="19" width="3.5" height="43" fill="var(--navy)"/><rect x="17" y="40" width="3.5" height="22" fill="var(--yellow)"/><rect x="21" y="42" width="3.5" height="20" fill="var(--teal)"/>
    <rect x="35" y="37" width="3.5" height="25" fill="var(--navy)"/><rect x="39" y="18" width="3.5" height="44" fill="var(--yellow)"/><rect x="43" y="42" width="3.5" height="20" fill="var(--teal)"/>
    <rect x="57" y="27" width="3.5" height="35" fill="var(--navy)"/><rect x="61" y="37" width="3.5" height="25" fill="var(--yellow)"/><rect x="65" y="32" width="3.5" height="30" fill="var(--teal)"/>
    <rect x="79" y="17" width="3.5" height="45" fill="var(--navy)"/><rect x="83" y="32" width="3.5" height="30" fill="var(--yellow)"/><rect x="87" y="12" width="3.5" height="50" fill="var(--teal)"/>
    <text x="13" y="68">Category 1</text><text x="35" y="68">Category 2</text><text x="57" y="68">Category 3</text><text x="79" y="68">Category 4</text>
  </svg>
  <div class="opt" style="top:34px"><span class="ico is-navy"></span><div><div class="h">Option <b>One</b></div><div class="note">Brief supporting note here.</div></div></div>
  <div class="opt" style="top:59px"><span class="ico is-yellow"></span><div><div class="h">Option <b>Two</b></div><div class="note">Brief supporting note here.</div></div></div>
  <div class="opt" style="top:84px"><span class="ico is-teal"></span><div><div class="h">Option <b>Three</b></div><div class="note">Brief supporting note here.</div></div></div>
  <div class="brand foot-logo">Veltrin</div><div class="copy">© 2022 Veltrin. All rights reserved.</div>
</section>
<section class="slide" style="left:380px;top:1049px">
  <div class="photo" style="right:0;top:0;width:60%;height:125px;background:linear-gradient(160deg,#c9d3da,#5d6b78 50%,#2b3440);border-top-left-radius:70% 50%;border-bottom-left-radius:70% 50%" role="img" aria-label="Photo looking up at glass office towers"></div>
  <div style="position:absolute;right:0;top:70px;width:35px;height:40px;background:var(--yellow);opacity:.8;border-radius:10px 0 0 10px"></div>
  <div class="brand" style="position:absolute;left:16px;top:50px;font-size:14px">Veltrin</div>
  <div class="contact"><b>Contact Us</b><br>☏ Phone Number Goes Here<br>✉ E-Mail Address Goes Here<br>◍ URL Address Goes Here</div>
  <div class="bottom-bar is-teal">© 2022 Veltrin. All rights reserved.</div>
</section>

</body>
</html>
```